Seasoned logs and kindling for sale

producing firewood from beech,ash,oak and silver birch,
Kindling is produce from a variety of seasoned softwoods

Industry/Entity Type

Firewood

Contact Information for Business Card

peter Calloway 07831226904
alan Frickley 07854317620
e-mail,peterc817@mailbrook.example

```html
<!DOCTYPE html>
<html lang="en">
<head>
<meta charset="utf-8">
<title>Seasoned Logs and Kindling – Business Card</title>
<link rel="stylesheet" href="https://fonts.googleapis.com/css2?family=Cabin:wght@500;600&display=swap">
<style>
  :root {
    --page-bg: #ffffff;
    --wood-light: #e8cf9e;
    --wood-mid: #dcbd86;
    --wood-dark: #cfa973;
    --ruler-dark: #5a3318;
    --ink-brown: #6a3a1c;
    --band-brown: #6b3e20;
    --band-text: #fbf3e6;
  }
  * { margin: 0; padding: 0; box-sizing: border-box; }
  html, body {
    width: 1200px;
    height: 844px;
    overflow: hidden;
    background: var(--page-bg);
  }
  .card {
    position: absolute;
    left: 60px;
    top: 64px;
    width: 1044px;
    height: 684px;
    overflow: hidden;
    font-family: "Cabin", "Trebuchet MS", sans-serif;
    color: var(--ink-brown);
  }
  .wood-surface {
    position: absolute;
    inset: 0;
    background: linear-gradient(175deg, var(--wood-light) 0%, var(--wood-mid) 55%, var(--wood-dark) 100%);
  }
  .ruler-edge {
    position: absolute;
    left: 0;
    top: 0;
    width: 100%;
    height: 26px;
    background: linear-gradient(180deg, var(--ruler-dark) 0%, rgba(90, 51, 24, 0.55) 45%, rgba(90, 51, 24, 0) 100%);
  }
  .tagline {
    position: absolute;
    left: 50px;
    top: 174px;
    font-size: 35px;
    font-weight: 500;
    line-height: 44px;
    letter-spacing: 1.4px;
    white-space: nowrap;
  }
  .contact {
    position: absolute;
    top: 472px;
  }
  .contact--left { left: 46px; }
  .contact--right { right: 44px; text-align: right; }
  .contact__name {
    font-size: 40px;
    font-weight: 500;
    line-height: 58px;
    letter-spacing: 0.8px;
    padding-left: 36px;
  }
  .contact--right .contact__name { padding-left: 0; }
  .contact__phone {
    display: flex;
    align-items: center;
    gap: 4px;
    font-size: 43px;
    font-weight: 500;
    line-height: 58px;
    letter-spacing: 0.6px;
  }
  .contact--right .contact__phone { justify-content: flex-end; }
  .phone-icon { width: 32px; height: 42px; }
  .email-band {
    position: absolute;
    left: 0;
    bottom: 0;
    width: 100%;
    height: 74px;
    background: var(--band-brown);
    color: var(--band-text);
    font-size: 30px;
    font-weight: 500;
    display: flex;
    align-items: center;
    justify-content: center;
    letter-spacing: 0.8px;
  }
</style>
</head>
<body>
  <div class="card">
    <div class="wood-surface" role="img" aria-label="Light oak wood grain background"></div>
    <div class="ruler-edge" role="img" aria-label="Measuring ruler tick marks along the top edge"></div>

    <p class="tagline">
      Producing Firewood from<br>
      Beech, Ash, Oak and Silver Birch,<br>
      kindling is produce from a variety of seasoned softwoods
    </p>

    <div class="contact contact--left">
      <div class="contact__name">Peter Calloway</div>
      <div class="contact__phone">
        <svg class="phone-icon" viewBox="0 0 16 20" aria-hidden="true">
          <path fill="var(--ink-brown)" d="M5 1 L7.5 5.2 L5.6 7 Q6.3 11 9 13.4 L11 12 L14.6 15.6 L12.4 18.6 Q8 19.5 4.4 14.6 Q1.2 9.6 2.2 3.6 Z"/>
        </svg>
        <span>07831226904</span>
      </div>
    </div>

    <div class="contact contact--right">
      <div class="contact__name">Alan Frickley</div>
      <div class="contact__phone">
        <svg class="phone-icon" viewBox="0 0 16 20" aria-hidden="true">
          <path fill="var(--ink-brown)" d="M5 1 L7.5 5.2 L5.6 7 Q6.3 11 9 13.4 L11 12 L14.6 15.6 L12.4 18.6 Q8 19.5 4.4 14.6 Q1.2 9.6 2.2 3.6 Z"/>
        </svg>
        <span>07854317620</span>
      </div>
    </div>

    <div class="email-band">e-mail: peterc817@mailbrook.example</div>
  </div>
</body>
</html>
```